Automotive Locksmiith company needs a website design and mobile website

We need a website design and a mobile design for an automotive locksmith company called Halvern Keyworks LLC.We are based in the center of the Dallas-Fort Worth Metroplex. We have a website that was directed more towards the towing services we also offer. We would like to have it more towards our locksmith products. Our main services include:
Auto keys duplication
Cutting of new car keys
Car Lockouts
Laser key replacement
Cutting keys by code
Broken key extractions
Production of transponder keys
Key fob programming
Door lock repairs
Ignition repairs/replacement
We work on 95% of the automotive market that includes Vorla, Tessin, QRT, Pembrook, Marquenne, Dunmoral, Brask, VX, Sorvalo, Kelto, Zephrane, Oru, Hadley, Norax, Tabori, Valdrenne, Quillon, Pipo, Runel Okarawe , Brevik, Solumé, Drennhofer, Kestra.
We are one of the most affordable services in the DFW area . Our prices for transponder copies start at $35 per key. We provide services for high-end vehicles also as QRT and Valdrenne. We can program the new proximity keys for Tabori Vehicles 2013-up. We also work on the new Pell Vehicles 20-13 and up including the Pell Arden head remote key.
We would like to have a similar style to the website we already have with the option to schedule an appointment on the mobile website. This mobile application will deliver an email when a new customer is requiring the service. It will ask for Year, Make, Model , Service to be performed( Key copy, Lockout, Lost Key, Change Ignition lock, change door lock, Other services.) Description of the service to be performed, Address, Select time of service.
Our current website is halvernkeyworks.example

Reason: Need pictures of webpages inside design (about us , location etc) and mobile pictures( how website looks in Quorra / android)

Automotive

• check word attachment

```html
<!DOCTYPE html>
<html lang="en">
<head>
<meta charset="utf-8">
<title>Halvern Keyworks – Mobile Site</title>
<link rel="stylesheet" href="https://fonts.googleapis.com/css2?family=Roboto:wght@400;700&family=Roboto+Condensed:wght@400;700&family=Reenie+Beanie&display=swap">
<style>
  :root {
    --page-bg: #dfe8dc;
    --screen-bg: #1c2129;
    --panel-bg: #20262e;
    --panel-edge: #2c333d;
    --field-bg: #2b323d;
    --text-light: #c9d0da;
    --text-muted: #8a94a2;
    --accent: #05a5cc;
    --white: #ffffff;
    --ink: #1a1d22;
  }
  * { box-sizing: border-box; margin: 0; padding: 0; }
  html, body { width: 1200px; height: 1200px; overflow: hidden; }
  body {
    background: var(--page-bg);
    font-family: "Roboto", Arial, sans-serif;
    display: flex; justify-content: center;
  }
  .mobile-site {
    width: 640px; height: 1200px;
    background: var(--screen-bg);
    overflow: hidden;
    display: flex; flex-direction: column;
  }
  .top-bar {
    display: flex; align-items: center; justify-content: space-between;
    padding: 16px 24px 8px;
  }
  .contact-line {
    display: flex; gap: 18px;
    font-family: "Roboto Condensed", sans-serif;
    font-size: 13px; color: var(--text-muted);
  }
  .contact-line span { display: flex; align-items: center; gap: 6px; }
  .menu-select {
    width: 250px; height: 32px; background: var(--white);
    display: flex; align-items: center; justify-content: space-between;
    padding: 0 12px; font-size: 12px; color: #555;
  }
  .site-header {
    display: flex; align-items: center; gap: 14px;
    padding: 22px 24px 26px;
    border-bottom: 6px solid #181c22;
  }
  .brand-mark { width: 40px; height: 40px; background: var(--accent); }
  .brand-name {
    font-family: "Roboto Condensed", sans-serif; font-weight: 700;
    font-size: 26px; color: var(--text-light); text-transform: uppercase;
  }
  .panel {
    margin: 18px 22px 0;
    background: var(--panel-bg);
    border: 1px solid var(--panel-edge);
    box-shadow: 0 0 0 6px #191d23;
  }
  .search-form { padding: 22px 24px 26px; }
  .field { margin-bottom: 16px; }
  .field-label {
    font-family: "Roboto Condensed", sans-serif; font-weight: 700;
    font-size: 20px; color: var(--text-light); margin-bottom: 8px;
  }
  .field-select {
    height: 50px; background: var(--field-bg);
    display: flex; align-items: center; justify-content: space-between;
    padding: 0 18px; font-size: 17px; color: var(--text-muted);
  }
  .search-button {
    margin-top: 10px; height: 64px; width: 100%;
    border: none; background: var(--accent); color: var(--white);
    font-family: "Roboto", sans-serif; font-weight: 700; font-size: 24px;
    box-shadow: 0 4px 0 #047f9e;
  }
  .intro { padding: 20px 24px 22px; }
  .intro-kicker { font-size: 14px; color: var(--text-muted); }
  .intro-title {
    font-family: "Roboto Condensed", sans-serif; font-weight: 700;
    font-size: 27px; color: var(--text-light); margin: 4px 0 10px;
  }
  .intro p { font-size: 11.5px; line-height: 1.4; color: var(--text-muted); margin-bottom: 6px; }
  .about {
    margin-top: 24px; flex: 1;
    background: var(--white); border-top: 6px solid var(--accent);
    padding: 22px 24px;
  }
  .about-head { display: flex; align-items: center; gap: 16px; }
  .about-title { font-family: "Reenie Beanie", cursive; font-size: 46px; color: var(--ink); }
  .about-rule { flex: 1; height: 8px; background: #e4e6e9; }
  .about-photo {
    margin-top: 12px; height: 120px;
    background: linear-gradient(180deg, #7f8ea6, #2e4a7c);
  }
</style>
</head>
<body>
  <main class="mobile-site">
    <div class="top-bar">
      <div class="contact-line">
        <span>
          <svg width="12" height="12" viewBox="0 0 24 24"><path fill="#05a5cc" d="M6.6 10.8a15 15 0 0 0 6.6 6.6l2.2-2.2a1 1 0 0 1 1-.25 11 11 0 0 0 3.6.6 1 1 0 0 1 1 1V20a1 1 0 0 1-1 1A17 17 0 0 1 3 4a1 1 0 0 1 1-1h3.5a1 1 0 0 1 1 1c0 1.25.2 2.45.6 3.6a1 1 0 0 1-.25 1z"/></svg>
          TEL: 555-014-2290
        </span>
        <span>
          <svg width="10" height="13" viewBox="0 0 20 26"><path fill="#05a5cc" d="M10 0a10 10 0 0 0-10 10c0 7 10 16 10 16s10-9 10-16A10 10 0 0 0 10 0zm0 14a4 4 0 1 1 0-8 4 4 0 0 1 0 8z"/></svg>
          ADD: 1420 CORVANE AVE, DALLAS, TX 75000
        </span>
      </div>
    </div>
    <header class="site-header">
      <div class="brand-mark"></div>
      <div class="brand-name">Halvern Keyworks</div>
      <div style="flex:1"></div>
      <div class="menu-select">Menu <span>▾</span></div>
    </header>

    <form class="panel search-form">
      <div class="field"><div class="field-label">Year :</div><div class="field-select">Any <span>▾</span></div></div>
      <div class="field"><div class="field-label">Make :</div><div class="field-select">Any <span>▾</span></div></div>
      <div class="field"><div class="field-label">Model :</div><div class="field-select">Any <span>▾</span></div></div>
      <div class="field"><div class="field-label">Service to be performed :</div><div class="field-select">Any <span>▾</span></div></div>
      <button class="search-button" type="button">Search</button>
    </form>

    <section class="panel intro">
      <div class="intro-kicker">Professional Automotive Locksmith Service.</div>
      <h1 class="intro-title">Special Price For Used Car Dealerships!</h1>
      <p>We are a locally owned company with over 6 years of experience in the automotive industry. We provide towing and automotive locksmith services to the Dallas Ft-Worth Area. Our main goal is to provide unmatched customer service both to the client and your customer. You will appreciate the value of our professional approach to all your automotive needs. Our experienced staff will always be eager to assist you. We look forward to being your reliable business partner when your locksmith needs arise.</p>
      <p>Our business relationships with clients are warm, friendly and sincere. Our valued clients count on us to deliver excellent service and we're obliged to deliver above and beyond! We want every interaction you have with Halvern Keyworks LLC to be refreshing and delightful, especially given the circumstances that brought you to us! We eliminate stress or incident.</p>
    </section>

    <section class="about">
      <div class="about-head">
        <h2 class="about-title">About Us</h2>
        <div class="about-rule"></div>
      </div>
      <div class="about-photo" role="img" aria-label="Photo of a technician at work"></div>
    </section>
  </main>
</body>
</html>
```